Poster Design Project - Front Window Poster for IT Business

Design a poster to be displayed in the front window of our office.
To include the following text:
Brightlane Systems Group
Servers & Networks
Deskora 720
Cloud Solutions
Helpdesk Services & Support
Network Audits
Disaster Recovery
IT Consulting
Contact details to be shown on the poster:
www.tk.com.au
02 5183 6214
Please also include the logo and related colour scheme.
Needs to look professional and easy to read from the street.
Must be in A1 format, printable through prontoleaf.

```html
<!DOCTYPE html>
<html lang="en">
<head>
<meta charset="utf-8">
<title>TK Technology Solutions – Window Poster</title>
<link rel="stylesheet" href="https://fonts.googleapis.com/css2?family=Arimo:wght@400;700&display=swap">
<style>
  :root {
    --night: #0a0f1c;
    --deep-blue: #0b2a8a;
    --glow-blue: #2f6de0;
    --brand-blue: #2447c4;
    --ink: #111111;
    --paper: #ffffff;
    --tile-light: #5cc8f5;
    --tile-dark: #1f3fae;
    --footer: #0d0d0f;
  }
  * { margin: 0; padding: 0; box-sizing: border-box; }
  html, body { width: 854px; height: 1200px; overflow: hidden; background: var(--night); }
  .poster {
    position: relative;
    width: 854px;
    height: 1200px;
    font-family: "Arimo", Arial, sans-serif;
    background:
      radial-gradient(ellipse 420px 700px at 100% 40%, rgba(47,109,224,0.75), transparent 70%),
      radial-gradient(ellipse 700px 160px at 50% 100%, rgba(47,109,224,0.0), transparent),
      linear-gradient(180deg, #0c1630 0%, var(--night) 60%, #0c1a44 82%, var(--night) 100%);
    overflow: hidden;
  }
  .backdrop-glow {
    position: absolute;
    left: 0; top: 880px;
    width: 854px; height: 160px;
    background: radial-gradient(ellipse 460px 90px at 50% 50%, rgba(60,120,255,0.85), transparent 75%);
  }
  .sheet {
    position: absolute;
    left: 66px; top: 0;
    width: 721px; height: 988px;
    background: var(--paper);
    box-shadow: 0 10px 30px rgba(0,0,0,0.6);
  }
  .brand {
    position: absolute;
    left: 0; top: 110px;
    width: 100%;
    text-align: center;
    color: var(--brand-blue);
    font-weight: 700;
    font-size: 76px;
    line-height: 1.1;
  }
  .contact-line {
    position: absolute;
    left: 0; top: 314px;
    width: 100%;
    text-align: center;
    color: var(--brand-blue);
    font-weight: 700;
    font-size: 34px;
    word-spacing: 6px;
  }
  .contact-line span + span { margin-left: 20px; }
  .services {
    position: absolute;
    left: 17px; top: 418px;
    list-style: none;
  }
  .service {
    display: flex;
    align-items: center;
    height: 64px;
    font-weight: 700;
    font-size: 40px;
    color: var(--ink);
  }
  .service::before {
    content: "";
    width: 62px; height: 42px;
    margin-right: 10px;
    flex: none;
    background: linear-gradient(90deg, var(--tile-light), var(--tile-dark));
  }
  .footer {
    position: absolute;
    left: 0; top: 1032px;
    width: 854px; height: 168px;
    background: var(--footer);
  }
  .footer-contact {
    position: absolute;
    left: 52px; top: 46px;
    color: var(--paper);
    font-weight: 700;
    font-size: 30px;
    line-height: 1.3;
  }
  .footer-brand {
    position: absolute;
    right: 42px; top: 62px;
    color: var(--paper);
    font-weight: 700;
    font-size: 24px;
  }
</style>
</head>
<body>
  <div class="poster">
    <div class="backdrop-glow"></div>
    <section class="sheet">
      <h1 class="brand">TK Technology<br>Solutions</h1>
      <p class="contact-line"><span>www.tk.com.au</span><span>02 5183 6214</span></p>
      <ul class="services">
        <li class="service">Brightlane Systems Group</li>
        <li class="service">Servers &amp; Networks</li>
        <li class="service">Deskora 720</li>
        <li class="service">Cloud Solutions</li>
        <li class="service">Helpdesk Services &amp; Support</li>
        <li class="service">Network Audits</li>
        <li class="service">Disaster Recovery</li>
        <li class="service">IT Consulting</li>
      </ul>
    </section>
    <footer class="footer">
      <p class="footer-contact">www.tk.com.au<br>02 5183 6214</p>
      <p class="footer-brand">TK Technology Solutions</p>
    </footer>
  </div>
</body>
</html>
```